Informative brochure for college admissions prep service

Take the attached prose and images and design an attractive brochure. The color scheme should use the Marlowe University colors (black, cardinal, and white). The photos should all be grey scaled.

Cardinal

```html
<!DOCTYPE html>
<html lang="en">
<head>
<meta charset="utf-8">
<title>Halvorsen Admissions Brochure Spread</title>
<link rel="stylesheet" href="https://fonts.googleapis.com/css2?family=Source+Sans+3:wght@400;600;700;800&display=swap">
<style>
:root{
  --cardinal:#8f1a1e;
  --cardinal-dark:#6c1014;
  --black:#111;
  --blush:#f9dace;
  --ink:#231f20;
  --white:#fff;
}
*{margin:0;padding:0;box-sizing:border-box}
html,body{width:1200px;height:848px;overflow:hidden}
body{background:var(--blush);font-family:"Source Sans 3",sans-serif;color:var(--ink)}
.spread{position:relative;width:1200px;height:848px;overflow:hidden;background:var(--blush)}
.bands{position:absolute;inset:0;width:1200px;height:848px}
.heading{position:absolute;color:var(--white);font-weight:700;font-size:41px;letter-spacing:-.4px;line-height:1}
.results-heading{left:0;width:600px;text-align:center;top:56px}
.team-heading{left:620px;top:56px}
.results-intro{position:absolute;left:67px;top:103px;width:466px;color:var(--white);font-size:14px;line-height:17px;text-align:justify;text-align-last:center}
.stat{position:absolute;text-align:center}
.stat-value{display:block;font-weight:800;color:var(--cardinal);font-size:70px;line-height:56px;letter-spacing:-1px}
.stat-label{display:block;font-size:15.5px;line-height:19.3px;text-align:justify;text-align-last:center;margin-top:2px}
.stat-label.small{font-size:13.4px;line-height:17px}
.col-left{left:56px;width:204px}
.col-mid{left:333px;width:203px}
.team-intro{position:absolute;right:18px;top:71px;font-size:13.2px;line-height:14.2px;text-align:right}
.photo{position:absolute;background:linear-gradient(160deg,#9a9a9a,#4a4a4a)}
.founder-photo{left:628px;top:178px;width:112px;height:101px}
.founder{position:absolute;left:751px;top:176px;width:431px;font-size:13.2px;line-height:15px;text-align:justify}
.founder .name{color:var(--cardinal);font-weight:700}
.founder .school{color:var(--cardinal)}
.founder-story{position:absolute;left:620px;top:284px;width:562px;font-size:13.2px;line-height:15px;text-align:justify}
.consultants-heading{position:absolute;left:628px;top:363px;width:546px;color:var(--cardinal);font-weight:700;font-size:38px;letter-spacing:-.3px;line-height:1;white-space:nowrap}
.consultant{position:absolute;width:121px;text-align:center}
.consultant .photo{position:relative;display:block;width:121px;height:105px}
.consultant-name{display:block;margin-top:5px;color:var(--cardinal);font-weight:700;font-size:13px;line-height:13px;white-space:nowrap;margin-left:-24px;margin-right:-24px}
.consultant-school{display:block;font-weight:700;font-size:8.6px;line-height:10.5px;white-space:nowrap;margin-left:-24px;margin-right:-24px}
</style>
</head>
<body>
<main class="spread">
  <svg class="bands" viewBox="0 0 1200 848" aria-hidden="true">
    <polygon points="0,296 1200,28 1200,50 0,334" fill="var(--black)"/>
    <polygon points="0,0 1200,0 1200,42 0,308" fill="var(--cardinal)"/>
    <polygon points="1070,46 1200,20 1200,48" fill="var(--black)"/>
    <polygon points="0,0 380,0 0,76" fill="var(--cardinal-dark)"/>
    <polygon points="0,76 380,0 395,0 0,84" fill="var(--white)"/>
    <polygon points="0,768 600,848 0,848" fill="var(--black)"/>
    <polygon points="0,780 585,848 0,848" fill="var(--cardinal)"/>
  </svg>

  <h1 class="heading results-heading">OUR RESULTS:</h1>
  <p class="results-intro">At Halvorsen, we take a results-driven approach to college admissions. Our students get into top colleges at triple to quadruple the average acceptance rates at those colleges. The metrics we employ below are meaningful to our clients and show how the Halvorsen methodology can propel your child to his or her dream school.</p>

  <div class="stat col-left" style="top:326px">
    <span class="stat-value">28%</span>
    <span class="stat-label">Average acceptance rate of our clients at Oak League schools (versus the national average Oak League acceptance rate of 8%)</span>
  </div>
  <div class="stat col-left" style="top:493px">
    <span class="stat-value">57%</span>
    <span class="stat-label">Percent of our clients who received a merit scholarship from a university</span>
  </div>
  <div class="stat col-left" style="top:624px">
    <span class="stat-value">65%</span>
    <span class="stat-label small">Percent of our clients who gained admission to a Top 10 Business Program (according to National College Review)</span>
  </div>

  <div class="stat col-mid" style="top:256px">
    <span class="stat-value">69%</span>
    <span class="stat-label">Percent of our clients who gained admission to a Top 25 university (according to National College Review)</span>
  </div>
  <div class="stat col-mid" style="top:400px">
    <span class="stat-value">93%</span>
    <span class="stat-label">Percent of our clients who gained admission to a Top 50 university (according to National College Review)</span>
  </div>
  <div class="stat col-mid" style="top:547px">
    <span class="stat-value">72%</span>
    <span class="stat-label small">Percent of our clients who gained admission to a Top 10 Computer Science or Engineering Program (according to National College Review)</span>
  </div>
  <div class="stat col-mid" style="top:705px">
    <span class="stat-value">88%</span>
    <span class="stat-label small">Percent of our clients who gained admission to their flagship state school</span>
  </div>

  <h2 class="heading team-heading">OUR TEAM:</h2>
  <p class="team-intro">Our&nbsp;&nbsp;&nbsp;&nbsp;&nbsp;&nbsp;admission<br>consultants are all graduates<br>from the top universities and private<br>schools in the country, and have extensive writing<br>and editing experience. As recent alumni of America's top<br>schools, they have unique insight as to what distinguishes merely<br>adequate applications from excellent stand-out applications.</p>

  <div class="photo founder-photo" role="img" aria-label="Greyscale portrait of founder Daniel J. Ashby"></div>
  <p class="founder"><span class="name">Daniel J. Ashby, Founder</span><br><span class="school">Ashcombe University</span><br><span class="school">Wrenfield Law</span><br>Prior to founding Halvorsen Admissions Dan worked as an attorney for a prestigious law firm advising large corporations on business transactions. After leaving his law firm, Dan dedicated several years to working on behalf of the indigent in a variety of legal capacities.</p>
  <p class="founder-story">Dan's love for helping students to succeed began when he volunteered as a tutor during high school. While an undergraduate at Ashcombe University, he taught local students at a public high school. Later, while earning a law student at Wrenfield University, Dan excelled as a coach preparing law students for the bar examination.<br>Dan has more than 15 years of experience helping students at all levels conquer admissions.</p>

  <h2 class="consultants-heading">OUR ADMISSIONS CONSULTANTS:</h2>

  <figure class="consultant" style="left:660px;top:404px">
    <span class="photo" role="img" aria-label="Greyscale portrait of Marisol Okafor"></span>
    <figcaption><span class="consultant-name">Marisol Okafor</span><span class="consultant-school">Harwell University</span></figcaption>
  </figure>
  <figure class="consultant" style="left:840px;top:404px">
    <span class="photo" role="img" aria-label="Greyscale portrait of Julian Castellano"></span>
    <figcaption><span class="consultant-name">Julian Castellano</span><span class="consultant-school">Bramford University</span><span class="consultant-school">Calloway University</span></figcaption>
  </figure>
  <figure class="consultant" style="left:1019px;top:404px">
    <span class="photo" role="img" aria-label="Greyscale portrait of Peter Vasquez"></span>
    <figcaption><span class="consultant-name">Peter Vasquez</span><span class="consultant-school">Corrigan University</span><span class="consultant-school">Calloway University</span></figcaption>
  </figure>

  <figure class="consultant" style="left:660px;top:549px">
    <span class="photo" role="img" aria-label="Greyscale portrait of Elias Grunewald"></span>
    <figcaption><span class="consultant-name">Elias Grunewald</span><span class="consultant-school">Ashcombe University</span></figcaption>
  </figure>
  <figure class="consultant" style="left:840px;top:549px">
    <span class="photo" role="img" aria-label="Greyscale portrait of Tessa Lynn Morgan"></span>
    <figcaption><span class="consultant-name">Tessa Lynn Morgan</span><span class="consultant-school">Bramford University</span></figcaption>
  </figure>
  <figure class="consultant" style="left:1019px;top:549px">
    <span class="photo" role="img" aria-label="Greyscale portrait of Grant Whitaker"></span>
    <figcaption><span class="consultant-name">Grant Whitaker</span><span class="consultant-school">Northvale State University</span><span class="consultant-school">Yardley University</span></figcaption>
  </figure>

  <figure class="consultant" style="left:660px;top:699px">
    <span class="photo" role="img" aria-label="Greyscale portrait of Helena Kowal"></span>
    <figcaption><span class="consultant-name">Helena Kowal</span><span class="consultant-school">Harwell University</span></figcaption>
  </figure>
  <figure class="consultant" style="left:840px;top:699px">
    <span class="photo" role="img" aria-label="Greyscale portrait of Nora Lindqvist"></span>
    <figcaption><span class="consultant-name">Nora Lindqvist</span><span class="consultant-school">University of Westmere,</span><span class="consultant-school">Bayside</span></figcaption>
  </figure>
  <figure class="consultant" style="left:1019px;top:699px">
    <span class="photo" role="img" aria-label="Greyscale portrait of Claire Dunmore Hale" style="height:108px"></span>
    <figcaption><span class="consultant-name">Claire Dunmore Hale</span><span class="consultant-school">Corrigan University</span></figcaption>
  </figure>
</main>
</body>
</html>
```